Business Card Design

I would like a logo created for the top left corner of the card please. I would like a checkerboard in a dark navy with the edges fading out and one random bright orange square.
Updates

I have attached some further notes and a really rough sketch of what I am after.  Thank you. :)

Target Market(s)

Construction, mining, mechanical

Industry/Entity Type

Business

Contact Information for Business Card

KRW Fabrications Pty Ltd, Oscar Plunkett, P. 0413658207, F. 0753917260, E.oscar@krwfabrications.com.au, PO Box 87 WONGARA Q 4571, ABN 52983470611

Font styles to use
Sans Serif

Requirements
Must have
• Really Dark Navy
Really bright Orange

```html
<!DOCTYPE html>
<html lang="en">
<head>
<meta charset="utf-8">
<title>Harlow business card design Sample</title>
<link rel="stylesheet" href="https://fonts.googleapis.com/css2?family=Noto+Sans&family=Oswald:wght@400&family=Questrial&family=Roboto+Condensed:wght@500&display=swap">
<style>
  :root {
    --navy: #1d1a55;
    --orange: #f15322;
    --green: #4f8a22;
    --green-dark: #2e7a22;
    --ink: #111111;
    --card-edge: #8a8a8a;
    --paper: #ffffff;
    --check-grey: #c4c4c4;
  }
  html, body {
    margin: 0;
    padding: 0;
    overflow: hidden;
    background: var(--paper);
  }
  .sheet {
    position: relative;
    width: 1200px;
    height: 961px;
    overflow: hidden;
    background: var(--paper);
  }
  .sheet__bar {
    position: absolute;
    left: 0;
    width: 1200px;
  }
  .sheet__bar--top { top: 0; height: 6px; background: var(--green); }
  .sheet__bar--bottom { bottom: 0; height: 7px; background: var(--green-dark); }
  .sheet__title {
    position: absolute;
    top: 26px;
    left: 0;
    width: 1200px;
    text-align: center;
    font-family: "Noto Sans", sans-serif;
    font-size: 16px;
    color: var(--ink);
    margin: 0;
    font-weight: 400;
  }
  .design-label {
    position: absolute;
    left: 120px;
    font-family: "Oswald", sans-serif;
    font-size: 15px;
    letter-spacing: 0.5px;
    color: var(--ink);
  }
  .design-label--a { top: 278px; }
  .design-label--b { top: 694px; }

  .card {
    position: absolute;
    left: 291px;
    width: 616px;
    height: 378px;
    border: 1px solid var(--card-edge);
    background: var(--paper);
    overflow: hidden;
    color: var(--navy);
  }
  .card--a { top: 134px; font-family: "Roboto Condensed", sans-serif; font-weight: 500; }
  .card--b { top: 570px; font-family: "Questrial", sans-serif; }

  .card__pattern {
    position: absolute;
    left: 0;
    top: 0;
    width: 228px;
    height: 378px;
    background:
      linear-gradient(to bottom, rgba(255,255,255,0) 40%, rgba(255,255,255,0.85) 100%),
      linear-gradient(to right, var(--check-grey) 0%, #e2e2e2 60%, rgba(255,255,255,0) 100%);
  }
  .card__brand {
    position: absolute;
    margin: 0;
    color: var(--navy);
    font-size: inherit;
  }
  .card--a .card__brand {
    left: 240px;
    top: 44px;
    width: 360px;
    font-size: 30px;
    font-weight: 500;
    text-align: right;
  }
  .card--b .card__brand {
    left: 300px;
    top: 30px;
    width: 290px;
    font-size: 28px;
    font-weight: 400;
    line-height: 1.2;
    text-align: center;
  }
  .card__person {
    position: absolute;
    margin: 0;
  }
  .card--a .card__person { left: 382px; top: 190px; font-size: 27px; line-height: 31px; }
  .card--b .card__person { left: 300px; top: 152px; width: 290px; text-align: center; font-size: 24px; line-height: 28px; }
  .card__name { display: block; text-transform: uppercase; color: var(--navy); }
  .card__mobile { display: block; color: var(--orange); }

  .card__contact {
    position: absolute;
    left: 36px;
    top: 188px;
    margin: 0;
    padding: 0;
    list-style: none;
    text-transform: uppercase;
  }
  .card--a .card__contact { font-size: 25px; line-height: 28px; }
  .card--b .card__contact { font-size: 23px; line-height: 28px; }
  .card__contact li { color: var(--navy); white-space: nowrap; }
  .card__contact .tag { color: var(--orange); }
  .card__contact .abn { color: var(--orange); }

  .card__stripe { position: absolute; left: 0; }
  .card--a .card__stripe--navy { top: 340px; width: 309px; height: 22px; background: var(--navy); }
  .card--a .card__stripe--orange { top: 340px; left: 309px; width: 307px; height: 22px; background: var(--orange); }
  .card--b .card__stripe--navy { top: 338px; width: 616px; height: 11px; background: var(--navy); }
  .card--b .card__stripe--orange { top: 349px; width: 616px; height: 11px; background: var(--orange); }
</style>
</head>
<body>
<main class="sheet">
  <div class="sheet__bar sheet__bar--top"></div>
  <h1 class="sheet__title">Harlow business card design Sample</h1>

  <div class="design-label design-label--a">DESIGN - A</div>
  <section class="card card--a">
    <div class="card__pattern" role="img" aria-label="Fading checkerboard brand pattern with one orange square"></div>
    <h2 class="card__brand">KRW Fabrications Pty Ltd</h2>
    <ul class="card__contact">
      <li>PO Box 87 WONGARA Q 4571</li>
      <li><span class="tag">P.</span> 0413 658 207</li>
      <li><span class="tag">F.</span> 07 5391 7260</li>
      <li><span class="tag">E.</span> oscar@krwfabrications.com.au</li>
      <li class="abn">ABN 52 983 470 611</li>
    </ul>
    <p class="card__person">
      <span class="card__name">Oscar Plunkett</span>
      <span class="card__mobile">0413 658 207</span>
    </p>
    <div class="card__stripe card__stripe--navy"></div>
    <div class="card__stripe card__stripe--orange"></div>
  </section>

  <div class="design-label design-label--b">DESIGN - B</div>
  <section class="card card--b">
    <div class="card__pattern" role="img" aria-label="Fading checkerboard brand pattern with one orange square"></div>
    <h2 class="card__brand">KRW FABRICATIONS<br>PTY LTD</h2>
    <p class="card__person">
      <span class="card__name">Oscar Plunkett</span>
      <span class="card__mobile">0413 658 207</span>
    </p>
    <ul class="card__contact">
      <li>PO Box 87 WONGARA Q 4571</li>
      <li><span class="tag">P.</span> 0413 658 207</li>
      <li><span class="tag">F.</span> 07 5391 7260</li>
      <li><span class="tag">E.</span> oscar@krwfabrications.com.au</li>
      <li class="abn">ABN 52 983 470 611</li>
    </ul>
    <div class="card__stripe card__stripe--navy"></div>
    <div class="card__stripe card__stripe--orange"></div>
  </section>

  <div class="sheet__bar sheet__bar--bottom"></div>
</main>
</body>
</html>
```